Menu Design Project for new restauranct concept

Design menu for new restaurant concept called Juniper's Burgers & Dogs. Logo is attached.

Industry/Entity Type

Restaurant

Requirements
Must have
• Menu items and pricing:

Burgers
Snack Burger $3.49
Snack Cheeseburger $3.99
Juniper's signature Burger $4.99
Juniper's signature Cheeseburger $5.49
Burger toppings: bacon, lettuce, tomato, onion, pickle, grilled onions, grilled mushrooms, grilled green peppers, jalapeƱo peppers.

Dogs
Hot Dog $2.99
Bacon Cheese Hot Dog $3.99
Slaw Dog $3.99
Kraut Dog $3.49
Chili Dog $3.99 with or with out cheese
Hot dogs are 100% beef

Other
Grilled Chicken Sandwich $5.99
Grilled Chicken Sandwich with cheese $6.49
(Same toppings as burgers)

French Fries $1.99

Loaded Potatos
The Plain Tater: $4.99 choose from: butter, sour cream, cheese, chives
The Garden Tater: $5.99 choose from: the Basic plus, broccoli & cheese, grilled mushrooms, onions, & peppers
The Rancher Tater: $6.99 choose from the Basic/Veggie plus: grilled chicken, chili, Philly cheesesteak, pulled pork.

Drinks
32oz. Drink $1.88
20oz. Drink $1.69

attached logo.
Nice to have
• love to incorporate the woodgrain backgound. It makes the logo look most like a cattle brand, which we like.

```html
<!DOCTYPE html>
<html lang="en">
<head>
<meta charset="utf-8">
<title>Juniper's Burgers &amp; Dogs – Restaurant Menu</title>
<link rel="stylesheet" href="https://fonts.googleapis.com/css2?family=Open+Sans:wght@400;600;700&display=swap">
<style>
  :root {
    --backdrop-top: #f4f6f5;
    --backdrop-bottom: #c4d2cf;
    --wood-dark: #3a1a12;
    --wood-mid: #5a2a1c;
    --wood-light: #6b3322;
    --panel: #2a1716;
    --band: #1a0f0e;
    --rule: #8a6a5a;
    --ink: #f3ece6;
    --ink-soft: #cdbfb6;
    --accent: #c0483f;
  }
  * { box-sizing: border-box; margin: 0; padding: 0; }
  html, body { width: 1200px; height: 900px; overflow: hidden; }
  body {
    background: linear-gradient(180deg, var(--backdrop-top), var(--backdrop-bottom));
    font-family: "Open Sans", Arial, sans-serif;
    color: var(--ink);
    position: relative;
  }
  .sheet {
    position: absolute;
    top: 90px;
    width: 480px;
    height: 720px;
    overflow: hidden;
    box-shadow: 0 6px 18px rgba(0,0,0,.25);
  }
  .sheet--cover { left: 90px; }
  .sheet--menu { left: 630px; }
  .woodgrain {
    position: absolute; inset: 0;
    background: linear-gradient(135deg, var(--wood-mid), var(--wood-dark) 55%, var(--wood-light));
  }
  .brand {
    position: absolute;
    left: 0; right: 0;
    display: flex; flex-direction: column; align-items: center;
    text-align: center;
  }
  .brand__mark {
    width: 96px; height: 96px;
    border: 4px solid var(--ink);
    border-radius: 50%;
    display: flex; align-items: center; justify-content: center;
    margin-bottom: 8px;
  }
  .brand__name {
    font-weight: 700;
    color: var(--ink);
    font-size: 19px;
    letter-spacing: .5px;
    line-height: 1.15;
  }
  .brand__sub { font-size: 10px; color: var(--ink); margin-top: 2px; }
  .sheet--cover .brand { top: 70px; }
  .sheet--cover .brand__mark { width: 130px; height: 130px; }
  .sheet--cover .brand__name { font-size: 22px; }
  .cover__footer {
    position: absolute; left: 0; right: 0; top: 580px;
    border-top: 1px solid var(--rule);
    text-align: center;
    font-size: 10px;
    padding-top: 14px;
    line-height: 1.5;
  }
  .cover__web {
    margin-top: 10px;
    border-top: 1px solid var(--rule);
    padding-top: 8px;
  }
  .cover__band {
    position: absolute; left: 0; right: 0; top: 660px; height: 24px;
    background: var(--band);
  }
  .sheet--menu .brand { top: 20px; }
  .sheet--menu .brand__mark { width: 70px; height: 70px; border-width: 3px; margin-bottom: 4px; }
  .sheet--menu .brand__name { font-size: 13px; }
  .menu__bar {
    position: absolute; left: 0; right: 0; top: 150px; height: 28px;
    background: var(--band);
    display: flex; justify-content: space-between; align-items: center;
    padding: 0 26px;
    font-size: 10px; letter-spacing: .5px;
  }
  .menu__panel {
    position: absolute; left: 0; right: 0; top: 178px; bottom: 62px;
    background: var(--panel);
    padding: 14px 30px 0 44px;
  }
  .menu__section { margin-bottom: 10px; }
  .menu__heading { font-size: 12.5px; font-weight: 700; text-transform: uppercase; margin-bottom: 2px; }
  .menu__row {
    display: flex; justify-content: space-between; gap: 14px;
    font-size: 9.5px; line-height: 13px; color: var(--ink-soft);
  }
  .menu__price { white-space: nowrap; }
  .menu__note { font-size: 9.5px; line-height: 13px; color: var(--accent); }
  .menu__delivery {
    position: absolute; left: 0; right: 0; bottom: 0; height: 62px;
    border-top: 1px solid var(--rule);
    display: flex; align-items: center; justify-content: center;
    font-size: 13px; font-weight: 600;
  }
</style>
</head>
<body>
  <section class="sheet sheet--cover">
    <div class="woodgrain" role="img" aria-label="Dark reddish-brown woodgrain plank background"></div>
    <div class="brand">
      <div class="brand__mark"><span class="brand__name">Juniper's</span></div>
      <div class="brand__name">Burgers &amp; Dogs</div>
      <div class="brand__sub">Restaurant Menu</div>
    </div>
    <div class="cover__footer">
      <div>418 Alder Row, Fernhaven, MD 20977</div>
      <div>Tel: 555-014-7730</div>
      <div class="cover__web">www.junipersburgersdogs.example</div>
    </div>
    <div class="cover__band"></div>
  </section>

  <section class="sheet sheet--menu">
    <div class="woodgrain" role="img" aria-label="Dark reddish-brown woodgrain plank background"></div>
    <div class="brand">
      <div class="brand__mark"><span class="brand__name">Juniper's</span></div>
      <div class="brand__name">Burgers &amp; Dogs</div>
      <div class="brand__sub">Restaurant Menu</div>
    </div>
    <div class="menu__bar"><span>MENU ITEMS</span><span>PRICE (IN $)</span></div>
    <div class="menu__panel">
      <div class="menu__section">
        <h2 class="menu__heading">Burgers</h2>
        <div class="menu__row"><span>Snack Burger</span><span class="menu__price">$3.49</span></div>
        <div class="menu__row"><span>Snack Cheeseburger</span><span class="menu__price">$3.99</span></div>
        <div class="menu__row"><span>Juniper's Signature Burger</span><span class="menu__price">$4.99</span></div>
        <div class="menu__row"><span>Juniper's Signature Cheeseburger</span><span class="menu__price">$5.49</span></div>
        <p class="menu__note">Burger toppings: bacon, lettuce, tomato, onion, pickle, grilled onions, grilled mushrooms, grilled green peppers, jalapeño peppers</p>
      </div>
      <div class="menu__section">
        <h2 class="menu__heading">Dogs</h2>
        <div class="menu__row"><span>Hot Dog</span><span class="menu__price">$2.99</span></div>
        <div class="menu__row"><span>Bacon Cheese Hot Dog</span><span class="menu__price">$3.99</span></div>
        <div class="menu__row"><span>Slaw Dog</span><span class="menu__price">$3.99</span></div>
        <div class="menu__row"><span>Kraut Dog</span><span class="menu__price">$3.49</span></div>
        <div class="menu__row"><span>Chili Dog (with or without cheese)</span><span class="menu__price">$3.99</span></div>
        <p class="menu__note">Hot dogs are 100% beef</p>
      </div>
      <div class="menu__section">
        <h2 class="menu__heading">Others</h2>
        <div class="menu__row"><span>Grilled Chicken Sandwich</span><span class="menu__price">$5.99</span></div>
        <div class="menu__row"><span>Grilled Chicken Sandwich with cheese</span><span class="menu__price">$6.49</span></div>
        <p class="menu__note">(Same toppings as burgers)</p>
      </div>
      <div class="menu__section">
        <div class="menu__row"><h2 class="menu__heading">French Fries</h2><span class="menu__price">$1.99</span></div>
      </div>
      <div class="menu__section">
        <h2 class="menu__heading">Loaded Potatoes</h2>
        <div class="menu__row"><span>The Plain Tater: choose from: butter, sour cream, cheese, chives</span><span class="menu__price">$4.99</span></div>
        <div class="menu__row"><span>The Garden Tater: choose from the Basic plus, broccoli &amp; cheese, grilled mushrooms, onions, &amp; peppers</span><span class="menu__price">$5.99</span></div>
        <div class="menu__row"><span>The Rancher Tater: choose from the Basic/Veggie plus: grilled chicken, chili, Philly cheesesteak, pulled pork</span><span class="menu__price">$6.99</span></div>
      </div>
      <div class="menu__section">
        <h2 class="menu__heading">Drinks</h2>
        <div class="menu__row"><span>32oz. Drink</span><span class="menu__price">$1.88</span></div>
        <div class="menu__row"><span>20oz. Drink</span><span class="menu__price">$1.69</span></div>
      </div>
    </div>
    <div class="menu__delivery">For Home Delivery Please Call on : 555-014-7730</div>
  </section>
</body>
</html>
```